Financial Services Business Card Design

We are a financial services company Based in London, offering Short term Funding Solutions for companies, raising anywhere between £20,000 and £25million pounds.

The Card must have a professional look as it is going to be handed out to professionals I.E Solicitors, Accountants, Company directors and Business owners.

See Attached our company Logo

Industry/Entity Type

Business

Contact Information for Business Card

Lewis Thorncroft
Suite 41
R K House
Bramblecote Lane
Watford
HP19 4QX

```html
<!DOCTYPE html>
<html lang="en">
<head>
<meta charset="utf-8">
<title>Quillmere Funding – Business Card</title>
<link href="https://fonts.googleapis.com/css2?family=Source+Sans+3:wght@400;600;700&display=swap" rel="stylesheet">
<style>
  :root {
    --backdrop: #000000;
    --card: #333438;
    --divider: #26272a;
    --brand-blue: #2272bf;
    --brand-green: #3aaa35;
    --text-light: #f2f2f2;
  }
  * { margin: 0; padding: 0; box-sizing: border-box; }
  html, body {
    width: 1200px; height: 900px; overflow: hidden;
    background: var(--backdrop);
    font-family: "Source Sans 3", "Myriad Pro", Arial, sans-serif;
  }
  .canvas { position: relative; width: 1200px; height: 900px; }
  .card {
    position: absolute; top: 271px;
    width: 457px; height: 281px;
    background: var(--card);
    border-radius: 14px;
  }
  .card--front { left: 137px; }
  .card--back { left: 626px; }

  .brand-mark {
    position: absolute; display: flex; flex-direction: column; align-items: center;
  }
  .brand-mark__dot {
    border-radius: 50%;
    background: var(--brand-green);
  }
  .brand-mark__name {
    color: var(--brand-blue); font-weight: 700;
    letter-spacing: 0.5px; line-height: 1.05; text-align: center;
  }
  .card--front .brand-mark { left: 40px; top: 86px; width: 176px; gap: 12px; }
  .card--front .brand-mark__dot { width: 54px; height: 54px; }
  .card--front .brand-mark__name { font-size: 24px; }
  .card--back .brand-mark { left: 0; top: 76px; width: 457px; gap: 14px; }
  .card--back .brand-mark__dot { width: 60px; height: 60px; }
  .card--back .brand-mark__name { font-size: 34px; }

  .divider {
    position: absolute; left: 222px; top: 78px;
    width: 1px; height: 136px; background: var(--divider);
  }
  .contact { position: absolute; left: 243px; top: 67px; color: var(--text-light); }
  .contact__name {
    color: var(--brand-green); font-size: 18px; font-weight: 600; margin-bottom: 14px;
  }
  .contact__address { font-size: 13.5px; line-height: 19px; margin-bottom: 15px; }
  .contact__list { list-style: none; font-size: 13.5px; line-height: 19px; }
  .contact__list li { display: flex; align-items: center; gap: 9px; }
  .contact__icon { width: 10px; height: 10px; fill: var(--brand-green); flex: none; }
</style>
</head>
<body>
<main class="canvas">
  <section class="card card--front" aria-label="Card front">
    <div class="brand-mark">
      <span class="brand-mark__dot"></span>
      <span class="brand-mark__name">QUILLMERE<br>FUNDING</span>
    </div>
    <span class="divider"></span>
    <div class="contact">
      <h1 class="contact__name">Lewis Thorncroft</h1>
      <p class="contact__address">Suite 41, R K House Bramblecote<br>Lane, Watford, HP19 4QX</p>
      <ul class="contact__list">
        <li>
          <svg class="contact__icon" viewBox="0 0 10 10" aria-hidden="true"><path d="M2 0.5 L3.6 2.8 L2.7 3.8 Q3.8 6 6.2 7.3 L7.2 6.4 L9.5 8 L8.4 9.6 Q4.5 9.5 1.8 6.5 Q0.3 4.5 0.4 1.7 Z"/></svg>
          (044)-318-2265
        </li>
        <li>
          <svg class="contact__icon" viewBox="0 0 10 10" aria-hidden="true"><path d="M0.5 2 H9.5 V8.5 H0.5 Z M1 2.4 L5 5.6 L9 2.4 V3.3 L5 6.5 L1 3.3 Z" fill-rule="evenodd"/></svg>
          info@youremail.com
        </li>
        <li>
          <svg class="contact__icon" viewBox="0 0 10 10" aria-hidden="true"><circle cx="5" cy="5" r="4.6"/><path d="M3 3 Q5 2 6 4 Q7 6 5 7.5" stroke="#333438" stroke-width="1" fill="none"/></svg>
          www.website.com
        </li>
      </ul>
    </div>
  </section>

  <section class="card card--back" aria-label="Card back">
    <div class="brand-mark">
      <span class="brand-mark__dot"></span>
      <span class="brand-mark__name">QUILLMERE FUNDING</span>
    </div>
  </section>
</main>
</body>
</html>
```